Short Stage Works Gathering

I need a poster design for our 2012 play festival called 'The Harlow Bay Gathering of Short Stage Works 2012'. We are a community theatre in Port Macquarie, NSW, Australia. A beautiful seaside town with Norfolk Pine Trees and lots of pelicans. Our website is at www.curtaincallstage.org.au for more info. Our logo colours are a vibrant navy blue, red and yellow. The poster would need to depict drama, theatre, our logo, fun, and excitement. The dates are 8 - 10 June 2012. For more information e-mail r.m.dunwell@tidemail.com

Target Market(s)

All age groups and people interested in theatre

Industry/Entity Type

Festival

Requirements
Must have
• Title - Harlow Bay Gathering of Short Stage Works
For more information e-mail r.m.dunwell@tidemail.com
Dates - 8 - 10 June 2012
Curtain Call Stage Logo
Website Address - www.curtaincallstage.org.au
Nice to have
• Background could include a picture of a theatrical stage

```html
<!DOCTYPE html>
<html lang="en">
<head>
<meta charset="utf-8">
<title>Harlow Bay Gathering of Short Stage Works 2012</title>
<link rel="stylesheet" href="https://fonts.googleapis.com/css2?family=Parisienne&family=Arvo:wght@700&display=swap">
<style>
  :root {
    --wood-dark: #2a1409;
    --wood-mid: #5a3119;
    --wood-light: #6e3d21;
    --curtain-red: #d4151c;
    --curtain-deep: #8e0b10;
    --banner-red: #e3232b;
    --badge-yellow: #f3d21c;
    --ink-light: #ffffff;
    --mask-light: #f1f1f1;
    --mask-shade: #c9c9c9;
  }
  html, body {
    margin: 0;
    padding: 0;
    overflow: hidden;
    background: var(--wood-dark);
  }
  .poster {
    position: relative;
    width: 900px;
    height: 1200px;
    overflow: hidden;
    background:
      radial-gradient(ellipse at 50% 40%, var(--wood-light) 0%, var(--wood-mid) 45%, var(--wood-dark) 100%);
    font-family: "Parisienne", cursive;
    color: var(--ink-light);
  }
  .stage-curtain {
    position: absolute;
    left: 0;
    top: 0;
    width: 900px;
    height: 200px;
  }
  .theatre-banner {
    position: absolute;
    left: 95px;
    top: 150px;
    width: 730px;
    height: 120px;
  }
  .banner-name {
    position: absolute;
    left: 110px;
    top: 176px;
    width: 580px;
    text-align: center;
    font-family: "Arvo", serif;
    font-weight: 700;
    font-size: 24px;
    letter-spacing: 1.5px;
    color: var(--ink-light);
    transform: rotate(1.2deg);
    margin: 0;
  }
  .banner-address {
    position: absolute;
    left: 110px;
    top: 206px;
    width: 580px;
    text-align: center;
    font-family: "Arvo", serif;
    font-weight: 700;
    font-size: 12px;
    letter-spacing: 1px;
    color: var(--ink-light);
    transform: rotate(1.2deg);
    margin: 0;
  }
  .festival-title {
    position: absolute;
    left: 0;
    top: 248px;
    width: 900px;
    margin: 0;
    text-align: center;
    font-weight: 400;
    font-size: 92px;
    line-height: 112px;
  }
  .festival-title span { display: block; }
  .festival-title .title-join { font-size: 80px; line-height: 84px; }
  .drama-masks {
    position: absolute;
    left: 125px;
    top: 575px;
    width: 660px;
    height: 400px;
  }
  .event-details {
    position: absolute;
    left: 0;
    top: 1008px;
    width: 900px;
    text-align: center;
  }
  .event-details p { margin: 0; }
  .detail-contact { font-size: 30px; line-height: 50px; }
  .detail-dates { font-size: 34px; line-height: 58px; }
  .detail-web { font-size: 28px; line-height: 56px; }
</style>
</head>
<body>
<main class="poster">
  <svg class="stage-curtain" viewBox="0 0 900 200" role="img" aria-label="Red velvet stage curtain swags draped across the top">
    <defs>
      <linearGradient id="curtainFill" x1="0" y1="0" x2="0" y2="1">
        <stop offset="0" stop-color="var(--curtain-deep)"/>
        <stop offset="0.6" stop-color="var(--curtain-red)"/>
        <stop offset="1" stop-color="var(--curtain-deep)"/>
      </linearGradient>
    </defs>
    <path d="M0 0 H900 V195 C860 190 760 160 700 100 C600 150 300 150 200 100 C150 160 60 170 0 165 Z" fill="url(#curtainFill)"/>
  </svg>

  <svg class="theatre-banner" viewBox="0 0 730 120" aria-hidden="true">
    <polygon points="5,8 640,22 640,90 15,78" fill="var(--banner-red)"/>
    <rect x="628" y="22" width="90" height="90" fill="var(--badge-yellow)"/>
  </svg>
  <p class="banner-name">THE CURTAIN CALL STAGE INC</p>
  <p class="banner-address">Cnr Keel &amp; Anchor Sts</p>

  <h1 class="festival-title">
    <span>Harlow Bay Gathering</span>
    <span class="title-join">of</span>
    <span>Short Stage Works</span>
  </h1>

  <svg class="drama-masks" viewBox="0 0 660 400" role="img" aria-label="Pair of white comedy and tragedy theatre masks with red features">
    <defs>
      <radialGradient id="maskFill" cx="0.5" cy="0.45" r="0.6">
        <stop offset="0" stop-color="var(--mask-light)"/>
        <stop offset="1" stop-color="var(--mask-shade)"/>
      </radialGradient>
    </defs>
    <rect x="0" y="0" width="660" height="400" rx="60" fill="url(#maskFill)"/>
  </svg>

  <section class="event-details">
    <p class="detail-contact">For more information e-mail r.m.dunwell@tidemail.com</p>
    <p class="detail-dates">Dates - 8 - 10 June 2012</p>
    <p class="detail-web">www.curtaincallstage.org.au</p>
  </section>
</main>
</body>
</html>
```